Poster for a Bicycle show/Expo

We need a poster for a Bicycle show/Expo and sustainable transport. Exhibitors will sell bikes, cycling clothing, accessories, etc. ...
This show is annual and the Poster is for the 2015 edition.

The style must be modern, dynamic, bright colors.

Your concept must be compatible in a landscape format. (We will ourselves adaptations of different formats.)
Width: 210 mm
Height: 297 mm
It's necessary for us to have the source file (vector) for make, later, the different format (flyers, website, ...)

Content of the Poster:
- 1 big picture (no clip art)
- Big title: « Fête Roulix » (« Salon » or « Salon du » can be small and « Vélo » big.)
- Subtitle: « et de la mobilité douce »
- Date: « 8, 9 et 10 mai 2015 » or « 8-10 mai 2015 »
- Place: « Halle TRX - Quai Brenaz »
- Text line 1: « www.fete-roulix.ch - Entrée gratuite »
- Text line 2« Piste d’essais - Restauration sur place »
- Text line 3: « Ve 8 mai de 17h à 21h - Sa 9 mai de 10h à 20h - Di 10 mai de 10h à 18h »
- Please, leave a zone in the poster for sponsors logos
(The predominant information (most visible) are: « Fête Roulix » and « 8, 9 et 10 mai 2015 or 8-10 mai 2015 »)

Content of the big picture:
- from a cheap stock, like PixoBanq.com
- a bicycle in action or a detail of a bicycle (or a accessory) (no race bike)
- a modern picture with bright colors.
- if a person is on the picture, we prefer a men
- not an aerial view with cyclists in a landscape.

Some examples of poster of shows - with typo-title worked

http://www.bassinexpoville.com/Temp/IMG/F_a7c2e9b4d1f0836255e1b7a9c4d3f2e6812c9b0a4e5f7_200_296.png

http://qz4m.tolvanfoires.fr/Data/kmtolv_mer/block/F_9bd1c3e7f2a4605813c9e2d7b4a8f6c0d3e1a527f86c2.pdf
(page 2 of this PDF)

http://salons.marvelle-agenda.fr/images/marvelle-agenda/foires-salons/phototheque/expo-moto-brivanne/expo-moto-brivanne2012-affiche.jpg

http://www.drupaix.net/blog/wp-content/uploads/2007/03/affiche-foire-des-pages.jpg

http://www.voilemarine-club.com/wp-content/affiche-regate-2007.jpg

Hello,

For information, for your next versions, please, add the text "Piste d'essais".

- Text line 1: « www.fete-roulix.ch - Entrée gratuite »
- Text line 2: « Piste d’essais - Restauration sur place »
- Text line 3: « Ve 8 mai de 17h à 21h - Sa 9 mai de 10h à 20h - Di 10 mai de 10h à 18h »

Thanks,
Mathieu

Landscape

Sans Serif

```html
<!DOCTYPE html>
<html lang="fr">
<head>
<meta charset="utf-8">
<title>Fête Roulix 2015</title>
<link rel="stylesheet" href="https://fonts.googleapis.com/css2?family=Amaranth:wght@400;700&display=swap">
<style>
  :root {
    --paper: #ffffff;
    --ink: #111111;
    --sun-orange: #fbb900;
    --sun-yellow: #fff36a;
    --shadow-black: #151515;
  }
  * { margin: 0; padding: 0; box-sizing: border-box; }
  html, body { width: 1200px; height: 848px; overflow: hidden; background: var(--paper); }
  .poster {
    position: relative;
    width: 1200px;
    height: 848px;
    overflow: hidden;
    background: var(--paper);
    font-family: "Amaranth", sans-serif;
    color: var(--ink);
  }
  .hero-art {
    position: absolute;
    left: 330px;
    top: 0;
    width: 870px;
    height: 848px;
  }
  .event-info {
    position: absolute;
    left: 34px;
    top: 296px;
    font-weight: 700;
    line-height: 1;
  }
  .event-title { font-size: 80px; letter-spacing: 1px; }
  .event-subtitle { font-size: 37px; margin-top: 8px; }
  .event-dates { font-size: 54px; margin-top: 10px; }
  .event-venue { font-size: 23px; margin-top: 16px; }
  .opening-hours { list-style: none; margin-top: 32px; font-size: 25px; }
  .opening-hours li { margin-bottom: 12px; }
  .footer-line {
    position: absolute;
    right: 34px;
    bottom: 12px;
    font-size: 14px;
    font-weight: 700;
  }
</style>
</head>
<body>
<main class="poster">
  <svg class="hero-art" viewBox="0 0 870 848" role="img" aria-label="Illustration: silhouette noire d'un cycliste en action devant de grands disques orange et jaune">
    <defs>
      <radialGradient id="heroTone" cx="0.55" cy="0.5" r="0.65">
        <stop offset="0" stop-color="#2a2a2a"/>
        <stop offset="0.45" stop-color="#fbb900"/>
        <stop offset="0.8" stop-color="#fbc400"/>
        <stop offset="1" stop-color="#fff36a"/>
      </radialGradient>
    </defs>
    <path d="M470 0 H870 V848 H190 C120 760 110 660 150 560 C170 480 150 400 230 300 C300 200 380 120 470 0 Z" fill="url(#heroTone)"/>
  </svg>

  <section class="event-info">
    <h1 class="event-title">Fête Roulix</h1>
    <p class="event-subtitle">et de la mobilité douce</p>
    <p class="event-dates">8 – 10 mai 2015</p>
    <p class="event-venue">Halle TRX — Quai Brenaz</p>
    <ul class="opening-hours">
      <li>Ve 8 mai de 17h à 21h</li>
      <li>Sa 9 mai de 10h à 20h</li>
      <li>Di 10 mai de 10h à 18h</li>
    </ul>
  </section>

  <p class="footer-line">www.fete-roulix.ch - Entrée gratuite - Restauration sur place</p>
</main>
</body>
</html>
```